Buch-/eBook-Cover für Frauen zwischen 16-35
Zielgruppe
MLT/ Mellow Lantern Typesetting. Ich suche Unterstützung für die Erstellung eines Buchcovers für Frauen zwischen 16-35.
Aufgabenstellung
Ich habe eine Zusammenfassung des Projektes in dem beigefügten Word Dokument zusammen mit Beispielcovern, Covern der Konkurrenz etc.

```html
<!DOCTYPE html>
<html lang="de">
<head>
<meta charset="UTF-8">
<title>Das große Wochenglück-Buch für beste Freundinnen – Cover</title>
<link rel="stylesheet" href="https://fonts.googleapis.com/css2?family=Parisienne&family=Lora:wght@400;500&display=swap">
<style>
  :root {
    --page-bg: #eef0f6;
    --sky-top: #7f79b8;
    --sky-upper: #a79bd3;
    --sky-middle: #e9bcd9;
    --sky-lower: #c9a6dc;
    --sky-bottom: #8c7fc2;
    --ink-deep: #3a2d5c;
    --ink-soft: #4a3f6b;
    --accent-pink: #e2649c;
    --accent-light: #fbe3ef;
    --shadow: rgba(58, 45, 92, 0.18);
  }
  * { box-sizing: border-box; margin: 0; padding: 0; }
  html, body {
    width: 1200px;
    height: 1200px;
    overflow: hidden;
    background: var(--page-bg);
  }
  .canvas {
    position: relative;
    width: 1200px;
    height: 1200px;
    display: flex;
    align-items: center;
    justify-content: center;
    gap: 60px;
  }
  .cover {
    position: relative;
    width: 500px;
    height: 760px;
    overflow: hidden;
    box-shadow: 0 18px 40px var(--shadow);
  }
  .cover-sky {
    position: absolute;
    inset: 0;
    background:
      radial-gradient(ellipse 70% 30% at 30% 18%, rgba(255,255,255,0.35), transparent 70%),
      radial-gradient(ellipse 80% 25% at 70% 62%, rgba(255,230,240,0.55), transparent 70%),
      linear-gradient(180deg,
        var(--sky-top) 0%,
        var(--sky-upper) 22%,
        var(--sky-middle) 52%,
        var(--sky-lower) 76%,
        var(--sky-bottom) 100%);
  }
  .cover-content {
    position: relative;
    height: 100%;
    display: flex;
    flex-direction: column;
    align-items: center;
    text-align: center;
  }
  .line { display: block; white-space: nowrap; }

  /* Front */
  .front-tagline {
    margin-top: 60px;
    font-family: "Lora", serif;
    font-size: 16px;
    line-height: 1.5;
    color: var(--ink-deep);
  }
  .front-title {
    margin-top: 96px;
    font-family: "Parisienne", cursive;
    font-weight: 400;
    font-size: 62px;
    line-height: 1.18;
    color: var(--ink-deep);
  }

  /* Back */
  .back-heading {
    margin-top: 48px;
    font-family: "Parisienne", cursive;
    font-weight: 400;
    font-size: 34px;
    line-height: 1.2;
  }
  .back-heading .lead { color: var(--accent-light); }
  .back-heading .hook { color: var(--accent-pink); }
  .back-body {
    margin-top: 40px;
    width: 400px;
    font-family: "Lora", serif;
    font-size: 15px;
    line-height: 1.6;
    color: var(--ink-soft);
  }
  .back-body p + p { margin-top: 22px; }
</style>
</head>
<body>
<main class="canvas">

  <section class="cover cover-front">
    <div class="cover-sky" role="img" aria-label="Pastellfarbener Abendhimmel mit violetten und rosa Wolken, kleiner Mond und Sterne am unteren Rand"></div>
    <div class="cover-content">
      <p class="front-tagline">
        <span class="line">Zusammen wachsen, lachen und</span>
        <span class="line">die Welt entdecken</span>
      </p>
      <h1 class="front-title">
        <span class="line">Das große</span>
        <span class="line">Wochenglück-</span>
        <span class="line">Buch für</span>
        <span class="line">beste</span>
        <span class="line">Freundinnen</span>
      </h1>
    </div>
  </section>

  <section class="cover cover-back">
    <div class="cover-sky" role="img" aria-label="Pastellfarbener Abendhimmel mit violetten und rosa Wolken, Sterne und kleiner Mond"></div>
    <div class="cover-content">
      <h2 class="back-heading">
        <span class="line lead">Von Alltag zu Abenteuer:</span>
        <span class="line hook">Entdeckt die Magie</span>
        <span class="line hook">gemeinsamer Erlebnisse</span>
      </h2>
      <div class="back-body">
        <p>Das Wochenglück-Buch für beste Freundinnen bietet euch 52 abwechslungsreiche Aktivitäten, die euch ein Jahr voller Spaß, Abenteuer und unvergesslicher Erinnerungen bescheren. Ein Jahr, das eure Freundschaft für immer stärken wird.</p>
        <p>Von spannenden Outdoor-Abenteuern bis hin zu kreativen DIY-Projekten – jede Woche bringt die perfekte Aktivität und die nötige Abwechslung in euren Alltag. Stärkt eure Freundschaft, lacht gemeinsam und genießt die kostbare Zeit miteinander.</p>
        <p>Entdeckt, wie viel Freude und Abwechslung das Leben bietet, wenn ihr es zusammen erlebt. Macht jede Woche zu etwas Besonderem – mit dem Wochenglück-Buch für beste Freundinnen!</p>
      </div>
    </div>
  </section>

</main>
</body>
</html>
```